plumbing & gas fitting business card design

We need a business card design for a plumbing & gas fitting company. The company covers commercial, domestic and maintenance work. We would like a modern design communicating efficiency and sophistication. preferred colours would include (red grey & black) or (green grey & black). Please DO NOT include any water droplets.

Varcoe Plumbing & Gas, Commercial Domestic & Maintenance, licence no. 418736K, ABN 57204918362, Phone 0417382965, Email varcoeplumbingandgas@tidemail.com

```html
<!DOCTYPE html>
<html lang="en">
<head>
<meta charset="utf-8">
<title>Varcoe Plumbing &amp; Gas – Business Card</title>
<link rel="stylesheet" href="https://fonts.googleapis.com/css2?family=Audiowide&display=swap">
<style>
  :root {
    --page-bg: #ffffff;
    --card-bg: #ececec;
    --pattern-light: #ebebeb;
    --pattern-mid: #e2e2e2;
    --ink: #0a0a0a;
  }
  html, body {
    margin: 0;
    padding: 0;
    width: 1200px;
    height: 1000px;
    overflow: hidden;
    background: var(--page-bg);
  }
  .canvas {
    position: relative;
    width: 1200px;
    height: 1000px;
  }
  .card {
    position: absolute;
    left: 49px;
    top: 166px;
    width: 1099px;
    height: 678px;
    overflow: hidden;
    background: var(--card-bg);
  }
  .card-pattern {
    position: absolute;
    inset: 0;
    width: 100%;
    height: 100%;
  }
  .card-content {
    position: absolute;
    left: 156px;
    top: 0;
    font-family: "Audiowide", sans-serif;
    font-weight: 400;
    color: var(--ink);
    line-height: 1;
  }
  .card-content p { margin: 0; position: absolute; left: 0; white-space: nowrap; }
  .business-name { top: 128px; font-size: 44px; letter-spacing: 1px; }
  .services     { top: 205px; font-size: 30px; letter-spacing: 0.5px; }
  .licence      { top: 255px; font-size: 30px; letter-spacing: 0.5px; }
  .abn          { top: 305px; font-size: 30px; letter-spacing: 0.5px; }
  .phone        { top: 433px; font-size: 30px; letter-spacing: 0.5px; }
  .email        { top: 513px; font-size: 29px; letter-spacing: 0; }
</style>
</head>
<body>
<main class="canvas">
  <section class="card">
    <svg class="card-pattern" viewBox="0 0 1099 678" preserveAspectRatio="none"
         role="img" aria-label="Light grey repeating background pattern of pipe elbows and gas flames">
      <defs>
        <linearGradient id="patternTone" x1="0" y1="0" x2="1" y2="1">
          <stop offset="0" stop-color="var(--pattern-mid)"/>
          <stop offset="0.5" stop-color="var(--pattern-light)"/>
          <stop offset="1" stop-color="var(--pattern-mid)"/>
        </linearGradient>
      </defs>
      <rect width="1099" height="678" fill="url(#patternTone)"/>
    </svg>
    <div class="card-content">
      <p class="business-name">Varcoe Plumbing &amp; Gas</p>
      <p class="services">Commercial Domestic &amp; Maintenance</p>
      <p class="licence">licence no. 418736K</p>
      <p class="abn">ABN 57204918362</p>
      <p class="phone">0417382965</p>
      <p class="email">varcoeplumbingandgas@tidemail.com</p>
    </div>
  </section>
</main>
</body>
</html>
```